Creative, Fun, Eye catching signage for new office - inspire and inform!

I am looking for a billboard sign, a smaller sign and a very small sign for parking spots. These will be located in our new office space. I have uploaded two logos, this way you can choose. I would love to see what it looks like with black behind the logo but am open to creative ideas. I would like the majority of the background to be black and/or white

1. Sign for over door – with five at the top like in the photo attached

The sign size is 2600mm (L) x 900mm (H)

Logo at the top then services to the right side
Social & Living Skills Programs
Support Workers
Respite/Supported Holidays
Exercise Physiology
Occupational Therapy
Speech Therapy
Psychology
Behavioural Therapy

I would like the design to tie in with the website and/or flyers/banners attached. Please also try and add 1800 452 917

2. Sign for glass roller door

745cm wide by 725cm high ( similar to what next door has without it saying parent )

Tellwick Logo
Drop Off Zone

Smaller signs for parking spots
1000cm wide, 60cm high

Tellwick logo Visitor Parking 24/7

I would like the design to be consistent across the three items so they work together but are not identical.

I have attached images showing what I am talking about in relation to the location of each sign.

Target Market(s)

Families, parents and people with disabilities

Industry/Entity Type

Disability and community service

Colors

Designer to choose colors to be used in the design.

Requirements
Must have
• White or black background - the logo and please use colours shown in the brochures and banners provided. Preferences are black white and yellow
Nice to have
• all of our services and website and/or 1800 452 917 on banner 1
Should not have
• I dont want it to be to busy please

```html
<!DOCTYPE html>
<html lang="en">
<head>
<meta charset="utf-8">
<title>Tellwick Signage Set</title>
<link rel="stylesheet" href="https://fonts.googleapis.com/css2?family=Kumbh+Sans:wght@500;600;700&family=Open+Sans:wdth,wght@75..100,600..800&display=swap">
<style>
  :root {
    --sign-black: #000000;
    --sign-yellow: #fdcd3b;
    --sign-white: #ffffff;
    --backdrop: #efefed;
    --ink: #0a0a0a;
  }
  html, body {
    margin: 0;
    padding: 0;
    width: 1200px;
    height: 947px;
    overflow: hidden;
    background: var(--backdrop);
  }
  .canvas {
    position: relative;
    width: 1200px;
    height: 947px;
  }
  .sign { position: absolute; }
  .sign > svg { position: absolute; inset: 0; display: block; }

  /* Door sign */
  .door-sign { left: 220px; top: 40px; width: 760px; height: 380px; }
  .door-sign .unit-number {
    position: absolute; left: 344px; top: 19px; width: 72px; height: 72px;
    display: flex; align-items: center; justify-content: center;
    font: 800 54px/1 "Open Sans", sans-serif; color: var(--ink);
  }
  .brand-name {
    position: absolute; margin: 0;
    font-family: "Open Sans", sans-serif; font-weight: 800;
    color: var(--sign-white); letter-spacing: 0.02em; text-transform: uppercase;
  }
  .door-sign .brand-name { left: 0; right: 0; top: 140px; text-align: center; font-size: 54px; line-height: 1; }
  .service-list {
    position: absolute; left: 10px; right: 10px; top: 262px;
    font: 600 13.5px/1 "Kumbh Sans", sans-serif; color: var(--ink);
  }
  .service-row {
    margin: 0 0 12px; padding: 0; list-style: none;
    text-align: center; white-space: nowrap;
  }
  .service-row li { display: inline; }
  .service-row li + li::before { content: "|"; font-weight: 500; padding: 0 7px; }
  .contact-line {
    position: absolute; left: 0; right: 0; top: 330px;
    display: flex; justify-content: center; gap: 34px;
    font: 700 17px/1 "Kumbh Sans", sans-serif; color: var(--ink);
  }
  .contact-line .phone { display: inline-flex; align-items: center; gap: 6px; }
  .contact-line svg { width: 18px; height: 18px; display: block; }

  /* Drop-off sign */
  .dropoff-sign { left: 110px; top: 530px; width: 300px; height: 280px; }
  .dropoff-sign .brand-name { left: 0; right: 0; top: 64px; text-align: center; font-size: 36px; line-height: 1; }
  .dropoff-sign .sign-label {
    position: absolute; left: 0; right: 0; top: 152px; margin: 0; text-align: center;
    font: 800 46px/1.05 "Open Sans", sans-serif; color: var(--ink); text-transform: uppercase;
  }

  /* Parking strip */
  .parking-sign { left: 520px; top: 650px; width: 590px; height: 46px; display: flex; }
  .parking-sign .strip-brand {
    width: 130px; background: var(--sign-black);
    display: flex; flex-direction: column; align-items: center; justify-content: center; gap: 2px;
  }
  .parking-sign .strip-brand .brand-dot { width: 9px; height: 9px; border-radius: 50%; background: var(--sign-yellow); }
  .parking-sign .brand-name { position: static; font-size: 12px; line-height: 1; }
  .parking-sign .strip-label {
    width: 310px; background: var(--sign-yellow);
    display: flex; align-items: center; justify-content: center;
    font: 700 36px/1 "Open Sans", sans-serif; font-stretch: 75%; color: var(--ink);
  }
  .parking-sign .strip-hours {
    flex: 1; background: var(--sign-black);
    display: flex; align-items: center; justify-content: center;
    font: 700 34px/1 "Open Sans", sans-serif; font-stretch: 75%; color: var(--sign-white);
  }
</style>
</head>
<body>
<main class="canvas">

  <section class="sign door-sign" aria-label="Over-door sign">
    <svg viewBox="0 0 760 380" width="760" height="380" aria-hidden="true">
      <path d="M0 110 H262 C266 40 318 0 380 0 C442 0 494 40 498 110 H760 V380 H0 Z" fill="var(--sign-black)"/>
      <path fill="var(--sign-yellow)" d="M0 208 C14 160 70 150 96 205 C110 190 140 190 160 214 C180 198 205 204 215 222 C240 200 270 206 285 225 C300 200 320 190 345 205 C360 175 410 170 425 210 C440 195 470 192 480 215 C500 200 530 205 540 228 C560 212 585 215 598 232 C615 205 650 200 662 228 C680 215 700 220 705 240 C720 205 750 200 760 225 V380 H0 Z"/>
      <circle cx="380" cy="55" r="36" fill="var(--sign-yellow)"/>
      <circle cx="380" cy="116" r="12" fill="var(--sign-yellow)"/>
    </svg>
    <div class="unit-number">5</div>
    <p class="brand-name">Tellwick</p>
    <div class="service-list">
      <ul class="service-row">
        <li>Social &amp; Living Skills Programs</li><li>Support Workers</li><li>Respite/Supported Holidays</li><li>Exercise Physiology</li>
      </ul>
      <ul class="service-row">
        <li>Occupational Therapy</li><li>Speech Therapy</li><li>Psychology</li><li>Behavioural Therapy</li>
      </ul>
    </div>
    <div class="contact-line">
      <span class="website">www.tellwick.com.au</span>
      <span class="phone">
        <svg viewBox="0 0 24 24" aria-hidden="true"><circle cx="12" cy="12" r="12" fill="var(--ink)"/><path d="M8.2 5.5l2 2.6-1.3 1.6c.8 1.8 2.2 3.3 4 4.2l1.6-1.3 2.6 2-1.2 2.4c-4.8-.6-8.6-4.4-9.2-9.2z" fill="var(--sign-yellow)"/></svg>
        1800 452 917
      </span>
    </div>
  </section>

  <section class="sign dropoff-sign" aria-label="Drop off zone sign">
    <svg viewBox="0 0 300 280" width="300" height="280" aria-hidden="true">
      <rect width="300" height="280" fill="var(--sign-yellow)"/>
      <path fill="var(--sign-black)" d="M0 0 H300 V128 C280 112 250 112 232 140 C215 125 195 128 185 140 C165 122 140 124 128 144 C118 130 100 132 92 140 C70 112 42 112 28 130 C18 118 8 120 0 128 Z"/>
      <circle cx="150" cy="34" r="14" fill="var(--sign-yellow)"/>
    </svg>
    <p class="brand-name">Tellwick</p>
    <p class="sign-label">Drop Off<br>Zone</p>
  </section>

  <section class="sign parking-sign" aria-label="Visitor parking sign">
    <div class="strip-brand"><span class="brand-dot"></span><span class="brand-name">Tellwick</span></div>
    <div class="strip-label">VISITOR PARKING</div>
    <div class="strip-hours">24/7</div>
  </section>

</main>
</body>
</html>
```